Design for a real estate wev portal

Contents and features of the site
---------------------------------
Website in 5 languages: French, Dutch, English, German, Spanish.
English name of the site: Lantern Nest Place
Main purpose of the site:
- allow people to rent their house/ appartment for flatsharing purposes.
- help people wanting to find a room in flatsharing
- help people to find additional roommates for their flatsharing
Key interaction sequence:
1. I create a "group" of people who have common interest/hobbies
2. People who have the same interests/hobbies join my group
3. I look for a house/appartment to host my group
Website structure will be the following:
- Home
- Groups
-- Look for a group
--- Join a group
-- Create a group
- Properties
-- Look for a house/appartement
-- Apply
- Sales conditions
- Contact
- My account
-- My profile
-- My groups OR my properties
Your mission
------------
The client has no graphical guidelines, simply a logo (see attached).
We need a (responsive compliant) design for the following pages (we expect PSD's from you. No HTML nor CSS):
1. homepage (see example and wireframe attached)
2. properties search result list (see wireframe attached)
3. "detailed" form for properties
4. groups search result list
5. "detailed" form for groups
6. my account page
FOR THE COMPETITION step we only expect from you the design of first 2 screens.
Based on that, we will select the designer who will win the project, and will have to design the 4 remaining screens.
Target Market(s)
B2C
Industry/Entity Type
Real Estate
Number of Pages Required
5+ page
Look and feel
Each slider illustrates characteristics of the customer's brand and the style your logo design should communicate.

```html
<!DOCTYPE html>
<html lang="en">
<head>
<meta charset="utf-8">
<title>Lantern Nest Place – Duplex a Valmont</title>
<link href="https://fonts.googleapis.com/css2?family=Lato:wght@400;700&display=swap" rel="stylesheet">
<style>
:root{
  --teal:#1595a5;
  --teal-dark:#0f8494;
  --green:#6bbf44;
  --label:#2a9bb0;
  --ink:#333;
  --line:#e2e2e2;
  --title-bg:#dbf0f4;
  --box-green:#dcefd6;
  --box-pink:#f3dede;
  --row-alt:#f4f4f4;
}
*{box-sizing:border-box;margin:0;padding:0}
html,body{width:826px;height:1200px;overflow:hidden;background:#fff;font-family:'Lato',sans-serif;color:var(--ink)}
.page{position:relative;width:826px;height:1200px}
.topbar{position:absolute;left:0;top:0;width:826px;height:26px;background:var(--teal)}
.topbar .social{position:absolute;left:111px;top:6px;display:flex;gap:6px}
.topbar .social span{width:13px;height:13px;border-radius:50%;background:#fff}
.topbar .social span.alt{background:var(--green)}
.topbar .create{position:absolute;left:170px;top:3px;height:20px;padding:0 10px;border-left:1px solid rgba(255,255,255,.25);border-right:1px solid rgba(255,255,255,.25);color:#fff;font-size:9px;line-height:20px}
.topbar .right{position:absolute;right:112px;top:3px;display:flex;gap:6px}
.topbar .right span{border:1px solid rgba(255,255,255,.3);color:#fff;font-size:9px;line-height:18px;padding:0 9px}
.mainnav{position:absolute;left:0;top:26px;width:826px;height:59px;border-bottom:1px solid var(--line)}
.mainnav a{position:absolute;top:24px;font-size:8.5px;color:#333;text-decoration:none}
.mainnav a.active{color:var(--teal);font-weight:700}
.brand{position:absolute;left:343px;top:14px;display:flex;align-items:center;gap:6px}
.brand i{width:16px;height:16px;border-radius:50%;background:var(--green)}
.brand b{font-size:17px;font-weight:700;color:var(--teal);line-height:1}
.titlebar{position:absolute;left:111px;top:98px;width:603px;height:31px;background:var(--title-bg);border:1px solid #c7e6ec}
.titlebar h1{position:absolute;left:10px;top:7px;font-size:13px;font-weight:400;color:#222}
.titlebar .save{position:absolute;right:4px;top:4px;width:61px;height:21px;background:var(--teal);color:#fff;font-size:8px;line-height:21px;padding-left:32px}
.titlebar .save svg{position:absolute;left:7px;top:4px}
.photo{position:absolute;left:111px;top:150px;width:302px;height:200px;border:1px solid #bbb;padding:5px}
.photo div,.thumb{background:linear-gradient(180deg,#4a90c8 0%,#e8eef2 45%,#2aa3d8 75%,#a8704a 100%)}
.photo div{width:100%;height:100%}
.thumbs{position:absolute;left:111px;top:360px;display:flex;gap:8px}
.thumb{width:70px;height:45px;border:1px solid #999}
.details{position:absolute;left:420px;top:150px;width:294px}
.details .row{display:flex;font-size:7.5px;line-height:12px;margin-bottom:15px}
.details dt{width:66px;text-align:right;color:var(--label);padding-right:7px;flex:none}
.details dd{color:#333}
.specs{position:absolute;left:111px;top:439px;width:603px;border:1px solid var(--line);border-collapse:collapse;font-size:7.2px}
.specs td{height:27px;white-space:nowrap;border-right:1px solid var(--line)}
.specs tr:nth-child(even){background:var(--row-alt)}
.specs .k{color:var(--label);text-align:right;padding-right:4px}
.specs .v{padding-right:6px}
.map{position:absolute;left:111px;top:607px;width:603px;height:207px;background:linear-gradient(90deg,#ece9e2 0%,#ece9e2 55%,#cfe5c1 62%,#e6ebdc 80%,#ece9e2 100%)}
.panels{position:absolute;left:111px;top:842px;display:flex;gap:8px}
.panel{width:146px;height:154px;border:1px solid #ddd;border-radius:3px;overflow:hidden}
.panel h2{height:25px;background:var(--box-green);font-size:10px;font-weight:400;line-height:25px;padding-left:11px;color:#333}
.panel.pink h2{background:var(--box-pink)}
.panel li{list-style:none;height:25.8px;border-top:1px solid var(--line);font-size:8px;line-height:25px;padding-left:11px;position:relative}
.panel li:first-child{border-top:none}
.panel .btn{position:absolute;right:3px;top:3px;background:var(--teal);color:#fff;font-size:7px;line-height:18px;padding:0 7px}
.footer{position:absolute;left:0;top:1027px;width:826px;height:119px;display:flex}
.footer .teal{width:413px;background:var(--teal)}
.footer .green{width:413px;background:var(--green)}
.fcol{position:absolute;top:1052px;color:#fff}
.fcol h3{font-size:11.5px;font-weight:700;letter-spacing:.3px;padding-bottom:4px;border-bottom:1px solid rgba(255,255,255,.7);display:inline-block;width:100px}
.fcol ul{margin-top:7px}
.fcol li{list-style:none;font-size:7.5px;line-height:13.3px;padding-left:11px;position:relative}
.fcol li::before{content:"";position:absolute;left:1px;top:5px;width:4px;height:4px;border-radius:50%;background:#fff}
.bottomnav{position:absolute;left:111px;top:1162px;display:flex;font-size:8px}
.bottomnav a{color:#333;text-decoration:none;padding:0 10px;border-left:1px solid #ccc;line-height:10px}
.bottomnav a:first-child{padding-left:0;border:none;color:var(--teal);font-weight:700}
.copy{position:absolute;left:110px;top:1183px;font-size:7.5px;color:#333}
.icons{position:absolute;left:563px;top:1168px;display:flex;gap:5px}
.icons span{width:17px;height:17px;border-radius:50%}
</style>
</head>
<body>
<div class="page">
  <div class="topbar">
    <div class="social"><span></span><span class="alt"></span><span></span></div>
    <div class="create">Create Your Group</div>
    <div class="right"><span>My Account</span><span>Login</span><span>English ⌄</span></div>
  </div>

  <nav class="mainnav">
    <a class="active" style="left:112px">Home</a>
    <a style="left:175px">Groups</a>
    <a style="left:243px">Look For A Group</a>
    <div class="brand"><i></i><b>Lantern Nest Place</b></div>
    <a style="left:521px">Properties</a>
    <a style="left:592px">Sales Conditions</a>
    <a style="left:684px">Contact</a>
  </nav>

  <div class="titlebar">
    <h1>Duplex a Valmont</h1>
    <div class="save"><svg width="13" height="12" viewBox="0 0 24 22"><path d="M12 21 2.5 11.6A5.8 5.8 0 0 1 12 4a5.8 5.8 0 0 1 9.5 7.6Z" fill="#fff"/></svg>Save</div>
  </div>

  <div class="photo"><div role="img" aria-label="Photo of a white two-storey villa with a swimming pool"></div></div>
  <div class="thumbs">
    <div class="thumb" role="img" aria-label="Villa exterior at dusk"></div>
    <div class="thumb" role="img" aria-label="Villa with pool"></div>
    <div class="thumb" role="img" aria-label="Poolside view"></div>
    <div class="thumb" role="img" aria-label="Living room interior"></div>
  </div>

  <dl class="details">
    <div class="row"><dt>Residence Type:</dt><dd>Other</dd></div>
    <div class="row"><dt>Street:</dt><dd></dd></div>
    <div class="row"><dt>Number:</dt><dd>0</dd></div>
    <div class="row"><dt>Zip code:</dt><dd>1480</dd></div>
    <div class="row"><dt>City:</dt><dd>Valmont-le-Bois</dd></div>
    <div class="row"><dt>Country:</dt><dd>Belgique</dd></div>
    <div class="row"><dt>Description:</dt><dd>Lorem ipsum dolor sit amet, consectetuer adipiscing elit, sed diam nonummy nibh euismod tincidunt ut laoreet dolore magna aliquam erat volutpat.</dd></div>
  </dl>

  <table class="specs">
    <tr><td class="k" style="width:78px">Availability date:</td><td class="v">30/11/2016</td><td class="k" style="width:110px">Number of toilets:</td><td class="v">3</td><td class="k" style="width:74px">Time lease:</td><td class="v">C</td><td class="k" style="width:118px">Included in charges:</td><td class="v" style="border:none">Eau - Electricite</td></tr>
    <tr><td class="k">Furnished:</td><td class="v">No</td><td class="k">Number of private toilets:</td><td class="v">2</td><td class="k">Type lease:</td><td class="v">24 months</td><td class="k">Smokers allowed:</td><td class="v" style="border:none">No</td></tr>
    <tr><td class="k">Living area:</td><td class="v">50</td><td class="k">Number of bathrooms:</td><td class="v">2</td><td class="k">Pact:</td><td class="v">Non</td><td class="k">Access for disabled persons:</td><td class="v" style="border:none">No</td></tr>
    <tr><td class="k">Common living area:</td><td class="v">50</td><td class="k">Number of private bathrooms:</td><td class="v">3</td><td class="k">Internal regulation:</td><td class="v">Non</td><td class="k">Pets allowed:</td><td class="v" style="border:none">No</td></tr>
    <tr><td class="k">Number of rooms:</td><td class="v">3</td><td class="k">Total rent:</td><td class="v">1200.00 €</td><td class="k">Common charges:</td><td class="v">50.00 €</td><td class="k">Domiciliating:</td><td class="v" style="border:none">No</td></tr>
  </table>

  <div class="map" role="img" aria-label="Map showing the property location"></div>

  <div class="panels">
    <div class="panel"><h2>Equipment</h2><ul><li>Diswasher</li><li>Washing Machine</li><li>Tumble Dryer</li><li>Wifi - TV</li><li>TV Distribution</li></ul></div>
    <div class="panel"><h2>Facilities</h2><ul><li>Garage</li><li>Garden</li><li></li><li></li><li></li></ul></div>
    <div class="panel pink"><h2>Equipment</h2><ul><li>Living Room</li><li>Toilet</li><li></li><li></li><li></li></ul></div>
    <div class="panel"><h2>Member Groups</h2><ul><li>Velo<span class="btn">See The Group</span></li><li></li><li></li><li></li><li></li></ul></div>
  </div>

  <div class="footer"><div class="teal"></div><div class="green"></div></div>
  <div class="fcol" style="left:26px"><h3>OCCUP GROUPS</h3><ul><li>Students</li><li>Young Workers</li><li>Full Time Workers</li></ul></div>
  <div class="fcol" style="left:166px"><h3>AGE GROUPS</h3><ul><li>Under 20 Yrs</li><li>20 Yrs - 30 Yrs</li><li>Over 30 yrs</li></ul></div>
  <div class="fcol" style="left:288px"><h3>GENDER GROUPS</h3><ul><li>Man &amp; Women</li><li>Man only</li><li>Women Only</li></ul></div>
  <div class="fcol" style="left:438px"><h3>CITIES</h3><ul><li>London</li><li>Paris</li><li>Brussels</li></ul></div>
  <div class="fcol" style="left:578px"><h3>RENT</h3><ul><li>Under $350</li><li>$350 - $600</li><li>Over $600</li></ul></div>
  <div class="fcol" style="left:700px"><h3>AVAILABILITY</h3><ul><li>Now</li><li>In a Month</li><li>In 3 Months</li></ul></div>

  <div class="bottomnav"><a>Home</a><a>Groups</a><a>Look For A Group</a><a>Properties</a><a>Sales Conditions</a><a>Contact</a></div>
  <div class="copy">© 2016 Lantern Nest Place. All Rights Reserved</div>
  <div class="icons">
    <span style="background:#2a4a8c"></span><span style="background:#2aa9e0"></span><span style="background:#1a6fa8"></span><span style="background:#e0453a"></span><span style="background:#c8261e"></span><span style="background:#555"></span><span style="background:#5aa040"></span>
  </div>
</div>
</body>
</html>
```